Flyer-Design für Tierphysiotherapie und Osteopathie
Zielgruppe
Tierphysiotherapie und Osteopathie Lotte Brenner
Aufgabenstellung
Text des gewünschten Flyers ist hochgeladen.
Ebenso die Visitenkarten und das Logo, sowie die Website - zur Orientierung von Farben, Schriftarten, etc.
Auch ein paar Bilder sind beigefügt.

```html
<!DOCTYPE html>
<html lang="de">
<head>
<meta charset="utf-8">
<title>Flyer Tierphysiotherapie Lotte Brenner</title>
<link href="https://fonts.googleapis.com/css2?family=Roboto+Condensed:wght@300;400;700&family=Oswald:wght@500&family=Open+Sans:wght@400&display=swap" rel="stylesheet">
<style>
  :root{
    --board:#dddedf;
    --paper:#ffffff;
    --taupe:#786d66;
    --amber:#f0ae2c;
    --ink:#6a5f58;
    --label:#1e1e1e;
  }
  *{margin:0;padding:0;box-sizing:border-box}
  html,body{width:1200px;height:849px;overflow:hidden;background:var(--board)}
  body{position:relative;font-family:"Roboto Condensed",Arial,sans-serif;color:var(--ink)}
  .board-label{position:absolute;left:145px;top:78px;font:400 10px "Open Sans",Arial,sans-serif;color:var(--label)}
  .flyer{position:absolute;top:123px;width:422px;height:598px;background:var(--paper);overflow:hidden;box-shadow:4px 5px 6px rgba(0,0,0,.35)}
  .flyer--front{left:145px}
  .flyer--back{left:632px}
  .photo{position:absolute}
  .header-shapes{position:absolute;left:0;top:0;width:422px;height:260px}
  .headline{position:absolute;left:26px;color:var(--amber);font-weight:300;line-height:1.18}
  .flyer--front .headline{top:210px;font-size:20px}
  .flyer--back .headline{top:143px;font-size:20.5px}
  .text{position:absolute;font-size:10px;line-height:1.4;font-weight:300}
  .text b{font-weight:700}
  .bullets{list-style:none}
  .bullets li{position:relative;padding-left:10px;margin-bottom:7px}
  .bullets li::before{content:"";position:absolute;left:0;top:5px;width:4px;height:4px;border-radius:50%;background:var(--amber)}
  .bullets--tight li{margin-bottom:0}
  .wordmark{position:absolute;display:flex;align-items:center;gap:6px;color:var(--taupe);font-size:14px;font-weight:300}
  .wordmark::before{content:"";width:8px;height:8px;border-radius:50%;background:var(--amber)}
  .contact-box{position:absolute;background:var(--amber);color:#fff;padding:11px 0 0 18px}
  .contact-box .name{font:500 16px "Oswald",Arial,sans-serif;letter-spacing:1px}
  .contact-box .role{font:400 5.5px "Open Sans",Arial,sans-serif;margin:4px 0 7px;letter-spacing:.3px}
  .contact-box .line{display:flex;align-items:center;gap:5px;font:400 5.5px "Open Sans",Arial,sans-serif;margin-bottom:4px;letter-spacing:.4px}
  .contact-box svg{width:6px;height:6px;fill:#fff}
  .accent{color:var(--amber);font-weight:700}
</style>
</head>
<body>
  <p class="board-label">Flyer zweiseitig A5</p>

  <section class="flyer flyer--front">
    <div class="photo" role="img" aria-label="Foto: Therapeutin mit einem braunen Pferd vor einer Holzscheune" style="left:0;top:0;width:422px;height:245px;background:linear-gradient(100deg,#b5694a 0%,#6b4a38 35%,#7d7a76 60%,#4f5a5d 100%)"></div>
    <svg class="header-shapes" viewBox="0 0 422 260" aria-hidden="true">
      <path d="M0,165 C100,195 230,232 422,220 L422,236 C300,252 150,262 0,246 Z" fill="var(--taupe)"/>
      <path d="M240,243 C320,240 392,222 422,192 L422,242 C360,252 300,252 240,245 Z" fill="var(--amber)"/>
      <path d="M0,246 C150,262 300,252 422,240 L422,260 L0,260 Z" fill="var(--paper)"/>
    </svg>
    <h1 class="headline">Ihr Tier in guten Händen</h1>

    <p class="text" style="left:25px;top:252px;font-size:11px;font-weight:400">Sie möchten:</p>
    <ul class="text bullets" style="left:40px;top:281px;width:175px">
      <li>Ihrem Jungtier <b>einen guten Start ins Leben</b> ermöglichen?</li>
      <li>Ihr Tier <b>langfristig fit</b> erhalten, um bis ins hohe Alter <b>viel Spaß</b> an gemeinsamen Unternehmungen zu haben?</li>
    </ul>
    <div class="wordmark" style="left:240px;top:300px">Tierphysiotherapie Lotte Brenner</div>
    <ul class="text bullets" style="left:40px;top:372px;width:340px">
      <li><b>bei Beschwerden im Bewegungsapparat</b> wie z.B. HD, ED, Bandscheibenvorfällen oder neurologischen Einschränkungen, nach Verletzungen oder Operationen <b>kompetent und mit viel Feingefühl</b> unterstützt werden?</li>
    </ul>

    <div class="photo" role="img" aria-label="Foto: Therapeutin behandelt das Bein eines Ponys auf einer Wiese" style="left:24px;top:428px;width:104px;height:148px;background:linear-gradient(180deg,#8fae6a 0%,#6e8f4a 45%,#9c6a45 60%,#4c7a38 100%);box-shadow:2px 3px 4px rgba(0,0,0,.3)"></div>
    <ul class="text bullets" style="left:140px;top:434px;width:230px">
      <li>Ihren <b>Sportler</b> professionell begleiten lassen?</li>
      <li>Durch <b>regelmäßigen Check Up</b>, frühzeitig handeln können, wenn doch mal was zwickt oder klemmt</li>
    </ul>
    <p class="text" style="left:148px;top:493px;font-size:11px;font-weight:400">Dann sind Sie bei mir genau Richtig!</p>

    <div class="contact-box" style="left:256px;top:522px;width:140px;height:76px">
      <p class="name">LOTTE BRENNER</p>
      <p class="role">Tierphysiotherapie &amp; Osteopathie</p>
      <p class="line"><svg viewBox="0 0 10 10"><path d="M2,0 L4,2 3,4 C4,6 5,7 6,7 L8,6 10,8 8,10 C4,10 0,6 0,2 Z"/></svg>0160/5528374</p>
      <p class="line"><svg viewBox="0 0 10 10"><path d="M0,2 H10 V8 H0 Z M0,2 L5,6 10,2" /></svg>info@tierphysio-brenner.de</p>
    </div>
  </section>

  <section class="flyer flyer--back">
    <div class="photo" role="img" aria-label="Foto: Therapeutin mit zwei Möpsen vor einem Stall" style="left:0;top:0;width:422px;height:255px;background:linear-gradient(90deg,#4d3a2c 0%,#6e5542 40%,#5a6f92 62%,#3d3530 100%)"></div>
    <svg class="header-shapes" viewBox="0 0 422 260" aria-hidden="true">
      <path d="M0,0 L64,0 C100,110 170,200 300,222 C340,228 390,228 422,224 L422,234 C330,252 180,262 0,256 Z" fill="var(--taupe)"/>
      <path d="M290,240 C350,234 395,224 422,212 L422,248 C370,252 320,248 290,240 Z" fill="var(--amber)"/>
      <path d="M0,256 C180,262 330,254 422,246 L422,260 L0,260 Z" fill="var(--paper)"/>
    </svg>
    <h1 class="headline">Ich heiße<br>Lotte Brenner und<br>bin Physiotherapeutin<br>und Osteopathin für Tiere</h1>

    <p class="text" style="left:25px;top:265px;width:372px;font-weight:400">Einschränkungen, Blockaden oder Schmerzen können viele Ursachen haben und äußern sich bei jedem Tier anders. Ihr Tier ist einzigartig, deshalb bekommen Sie bei mir die Behandlung, die zu Ihrem Tier und Ihnen passt!</p>
    <p class="text accent" style="left:25px;top:323px;width:210px">Neben der Arbeit mit meinen Händen biete ich unterschiedliche Therapieformen und Leistungen an wie z.B.</p>
    <ul class="text bullets bullets--tight" style="left:25px;top:364px;width:330px">
      <li>Lasertherapie</li>
      <li>Neurostim</li>
      <li>aktives und passives Bewegungstraining,</li>
      <li>gezielter Muskelaufbau</li>
      <li>und vieles mehr</li>
      <li>Ich gehe ganz besonders auf die speziellen Bedürfnisse Ihres Tiere ein und begleite Sie und Ihr Tier liebevoll und einfühlsam</li>
    </ul>
    <div class="wordmark" style="left:245px;top:368px">Tierphysiotherapie Lotte Brenner</div>
    <p class="text" style="left:25px;top:478px;font-size:10.5px;font-weight:400">Gemeinsam finden wir den besten Weg zu mehr Bewegung und Lebensfreude!</p>
    <p class="text" style="left:25px;top:506px;width:230px">Termine für Hunde und Kleintiere finden nach Vereinbarung in meiner Praxis in<br><span class="accent">74385 Lindenfeld, Am Mühlgraben 7</span><br>statt. Ich freue mich auf Sie!</p>
    <p class="text accent" style="left:25px;top:573px">www.tierphysio-brenner.de</p>

    <div class="contact-box" style="left:258px;top:524px;width:138px;height:74px">
      <p class="name">LOTTE BRENNER</p>
      <p class="role">Tierphysiotherapie &amp; Osteopathie</p>
      <p class="line"><svg viewBox="0 0 10 10"><path d="M2,0 L4,2 3,4 C4,6 5,7 6,7 L8,6 10,8 8,10 C4,10 0,6 0,2 Z"/></svg>0160/5528374</p>
      <p class="line"><svg viewBox="0 0 10 10"><path d="M0,2 H10 V8 H0 Z M0,2 L5,6 10,2" /></svg>info@tierphysio-brenner.de</p>
    </div>
  </section>
</body>
</html>
```